Corner Drift Curls - Automatic Wave Brush for 360 Wave Hairstyles

Logo Included. Single box 28 x 11 x 12 CM. Would like a photo on each corner, one of male with 360 Waves (google) and one of a female with 360 waves on the opposite corner same side or a square with 4 pictures of males/females. Urban/Slightly Luxury Appearance.

Industry/Entity Type

Hair And Beauty

Font styles to use
Serif
Sans Serif

Colors

Designer to choose colors to be used in the design.

Requirements
Must have
• ingle box 28 x 11 x 12 CM, Would like a photo on each corner, one of male with 360 Waves (google) and one of a female with 360 waves on the opposite corner same side or a square with 4 pictures of males/females.
Nice to have
• Urban/Luxury Feeling.
Should not have
• Females with long hairstyles, please google 360 Wave Hairstyle.

```html
<!DOCTYPE html>
<html lang="en">
<head>
<meta charset="utf-8">
<title>Corner Drift Curls – Wave Brush Box</title>
<link href="https://fonts.googleapis.com/css2?family=Montserrat:wght@600&family=Mrs+Saint+Delafield&family=Open+Sans:wght@400&display=swap" rel="stylesheet">
<style>
  :root{
    --page:#ffffff;
    --box:#0a0a0b;
    --frame:#8c6a3c;
    --accent:#e8202a;
    --brand-text:#f2f2f2;
    --dim:#1a1a1a;
    --skin-warm:#7a4a32;
    --skin-cool:#9aa2ab;
    --hair:#2a2420;
    --navy:#1c2450;
  }
  html,body{margin:0;padding:0;overflow:hidden;background:var(--page);}
  .canvas{position:relative;width:1200px;height:849px;overflow:hidden;background:var(--page);}
  .panel{position:absolute;left:196px;width:785px;background:var(--box);overflow:hidden;}
  .panel--top{top:80px;height:307px;}
  .panel--bottom{top:388px;height:337px;}
  .halftone{position:absolute;width:560px;height:420px;}
  .panel--top .halftone{left:-120px;top:-110px;
    background:radial-gradient(ellipse at 22% 26%, rgba(255,47,109,.75) 0%, rgba(255,47,109,.35) 28%, rgba(255,47,109,0) 62%);}
  .panel--bottom .halftone{right:-120px;top:-110px;
    background:radial-gradient(ellipse at 78% 26%, rgba(255,47,109,.75) 0%, rgba(255,47,109,.35) 28%, rgba(255,47,109,0) 62%);}
  .frame{position:absolute;border:1px solid var(--frame);}
  .panel--top .frame{left:24px;top:25px;width:736px;height:257px;}
  .panel--bottom .frame{left:24px;top:27px;width:736px;height:284px;}
  .brand{position:absolute;font-family:"Montserrat",sans-serif;font-weight:600;color:var(--brand-text);
    font-size:19px;line-height:23px;letter-spacing:1.5px;white-space:nowrap;display:flex;align-items:center;gap:9px;}
  .brand__dot{width:11px;height:11px;border-radius:50%;background:var(--accent);}
  .panel--top .brand{left:150px;top:110px;}
  .panel--bottom .brand{left:441px;top:156px;}
  .tagline{position:absolute;left:150px;top:206px;font-family:"Mrs Saint Delafield",cursive;
    color:var(--accent);font-size:34px;line-height:44px;white-space:nowrap;}
  .gallery{position:absolute;display:grid;grid-template-columns:1fr 1fr;grid-template-rows:1fr 1fr;}
  .panel--top .gallery{left:544px;top:46px;width:228px;height:232px;}
  .panel--bottom .gallery{left:54px;top:65px;width:239px;height:243px;}
  .photo--smile{background:linear-gradient(160deg,var(--hair) 0%,var(--skin-warm) 45%,#8d5a40 100%);}
  .photo--profile{background:linear-gradient(200deg,var(--skin-cool) 0%,var(--hair) 55%,#b89a88 100%);}
  .photo--fade{background:linear-gradient(170deg,#c9ccd3 0%,var(--hair) 45%,#6b4a3a 100%);}
  .photo--waves{background:linear-gradient(190deg,var(--navy) 0%,var(--hair) 50%,#5a3a2c 100%);}
  .dims{position:absolute;left:0;top:0;}
  .dim-label{position:absolute;font-family:"Open Sans",sans-serif;font-size:11px;color:var(--dim);}
</style>
</head>
<body>
<div class="canvas">
  <section class="panel panel--top">
    <div class="halftone" role="img" aria-label="Pink halftone dot pattern fading from the corner"></div>
    <div class="frame"></div>
    <div class="brand"><span class="brand__dot"></span>CORNER DRIFT CURLS</div>
    <div class="tagline">We'll style. You'll smile!</div>
    <div class="gallery">
      <div class="photo--smile" role="img" aria-label="Photo: smiling woman with short 360 waves"></div>
      <div class="photo--profile" role="img" aria-label="Photo: man in profile with 360 waves"></div>
      <div class="photo--fade" role="img" aria-label="Photo: man with 360 waves and skin fade, back view"></div>
      <div class="photo--waves" role="img" aria-label="Photo: woman in profile with deep 360 waves"></div>
    </div>
  </section>

  <section class="panel panel--bottom">
    <div class="halftone" role="img" aria-label="Pink halftone dot pattern fading from the corner"></div>
    <div class="frame"></div>
    <div class="gallery">
      <div class="photo--smile" role="img" aria-label="Photo: smiling woman with short 360 waves"></div>
      <div class="photo--profile" role="img" aria-label="Photo: man in profile with 360 waves"></div>
      <div class="photo--fade" role="img" aria-label="Photo: man with 360 waves and skin fade, back view"></div>
      <div class="photo--waves" role="img" aria-label="Photo: woman in profile with deep 360 waves"></div>
    </div>
    <div class="brand"><span class="brand__dot"></span>CORNER DRIFT CURLS</div>
  </section>

  <svg class="dims" width="1200" height="849" viewBox="0 0 1200 849" fill="none" stroke="#1a1a1a" stroke-width="1">
    <line x1="1001" y1="84" x2="1001" y2="383"/>
    <path d="M997 88 L1001 80 L1005 88 Z M997 379 L1001 387 L1005 379 Z" fill="#1a1a1a" stroke="none"/>
    <line x1="172" y1="392" x2="172" y2="721"/>
    <path d="M168 396 L172 388 L176 396 Z M168 717 L172 725 L176 717 Z" fill="#1a1a1a" stroke="none"/>
    <line x1="200" y1="735" x2="977" y2="735"/>
    <path d="M204 731 L196 735 L204 739 Z M973 731 L981 735 L973 739 Z" fill="#1a1a1a" stroke="none"/>
  </svg>
  <div class="dim-label" style="left:1010px;top:215px;">11CM</div>
  <div class="dim-label" style="left:124px;top:545px;">12CM</div>
  <div class="dim-label" style="left:587px;top:773px;">28CM</div>
</div>
</body>
</html>
```